FOOD PROCESSING KICK ASS LANDING PAGE

My client is a food processing center in Massachusetts. They help startups process and scale up their products. Here is a write up: The Eastern Ridge Produce Works Hub was created in 2001 to support new and growing food businesses as they navigate the path of bringing a food product to market. Our mission is to promote economic development through entrepreneurship, provide opportunities for sustaining local agriculture, and promote best practices for food producers. The ERPWH offers rental manufacturing space as well as co-packing services to food businesses in the commonwealth and beyond. We also work with local farms to make value-added products, like jams, sauces, pickles and purees. In addition to these services, our team also provides one-on-one counseling and technical assistance, supporting you with business planning, product development, regulatory compliance and more. I made a mock up and video description. Please watch video: https://clipreel-demo.net/watch/q8trLmWzuPx

General Inspiration:
Home page with banner photo: Co-Manufacturing - Brasswick Lodge
https://www.meadowpickprovisions.com/contact (contact page)
https://www.brightlanecoop.org/
https://www.hollowpinepantry.com
https://www.tillbrook.org/
https://www.gristhallworks.com/ (three key links on home page – kitchen, accelerator, on demand)
Business Services — Ladle Meal Studio: https://www.ladlemealstudio.com/business-services

Here is the page we are redesigning and see list of vendors below: https://www.nvtqbx.org/food-processing-center/

Only send landing page desktop view

Target Market(s)

Entrprenures

Industry/Entity Type

Food manufacturing

Number of Pages Required

1 page

Font styles to use
Sans Serif

Requirements
Must have
• Clean design that look amazing on mobile
Nice to have
• See mockup
Should not have
• See mockup

```html
<!DOCTYPE html>
<html lang="en">
<head>
<meta charset="utf-8">
<title>Eastern Ridge Produce Works Hub</title>
<link rel="stylesheet" href="https://fonts.googleapis.com/css2?family=Outfit:wght@400;500;600;700;800&display=swap">
<style>
:root{
  --orange:#d8602a;
  --green:#78b244;
  --slate:#4b6b7b;
  --peach:#f5e4dc;
  --dark:#333333;
  --ink:#2a2a2a;
  --muted:#666;
  --white:#fff;
}
*{box-sizing:border-box;margin:0;padding:0}
html,body{width:1200px;height:4569px;overflow:hidden}
body{font-family:'Outfit',sans-serif;color:var(--ink);background:var(--white);position:relative}
.block{position:absolute;left:0;width:1200px}
.abs{position:absolute}
.btn{position:absolute;background:var(--orange);color:var(--white);border-radius:30px;font-weight:600;display:flex;align-items:center;justify-content:center;gap:8px}
.ph{position:absolute}

/* header */
.site-header{top:0;height:89px;background:var(--white)}
.brand{left:235px;top:14px;display:flex;align-items:center;gap:8px}
.brand-dot{width:60px;height:60px;border-radius:50%;background:var(--orange)}
.brand-name{font-size:15px;font-weight:700;color:var(--orange)}
.contact-line{left:356px;top:10px;font-size:11px;color:var(--muted);display:flex;gap:28px;align-items:center}
.contact-line span{display:flex;gap:8px;align-items:center}
.social-top{left:896px;top:10px;display:flex;gap:18px}
.social-top i{width:10px;height:10px;border-radius:50%;background:var(--orange);display:block}
.nav{left:357px;top:56px;display:flex;gap:22px;font-size:11.5px;font-weight:600;color:var(--ink)}
.header-btn{left:842px;top:49px;width:130px;height:30px;font-size:11px}

/* hero */
.hero{top:89px;height:528px;background:linear-gradient(180deg,#56703c 0%,#6f8848 45%,#4b6330 100%)}
.hero-title{left:227px;top:100px;font-size:52px;line-height:62px;font-weight:800;color:var(--white);width:640px;text-transform:uppercase}
.hero-btn{left:226px;top:339px;width:128px;height:34px;font-size:11px}
.watch{left:385px;top:338px;display:flex;align-items:center;gap:14px;color:var(--white);font-size:11px;font-weight:600}
.watch-dot{width:36px;height:36px;border-radius:50%;background:var(--green);display:flex;align-items:center;justify-content:center}

.mission{left:230px;top:551px;width:742px;height:192px;background:var(--white);box-shadow:0 10px 30px rgba(0,0,0,.12);z-index:2}
.mission-photo{left:0;top:0;width:215px;height:192px;background:linear-gradient(135deg,#c94a32,#9aa3a6)}
.mission-text{left:274px;top:36px;width:430px;font-size:20px;line-height:30px;font-weight:600;color:var(--ink)}

/* about */
.about{top:760px;height:612px}
.about-photo-a{left:216px;top:135px;width:102px;height:213px;background:linear-gradient(160deg,#3b4a2c,#7b5240)}
.about-photo-b{left:318px;top:50px;width:282px;height:417px;background:linear-gradient(180deg,#b8302a,#d7d0c8 60%,#a8322a)}
.eyebrow{left:640px;top:62px;font-size:9px;font-weight:700;color:var(--orange)}
.about-title{left:640px;top:80px;width:360px;font-size:28px;line-height:38px;font-weight:600;color:var(--ink)}
.about-title em{font-style:normal;color:var(--green)}
.about-copy{left:640px;top:168px;width:340px;font-size:10.5px;line-height:22.5px;color:var(--muted)}

/* team */
.team{top:1372px;height:468px;background:var(--peach)}
.team h2{position:absolute;left:0;width:1200px;top:80px;text-align:center;font-size:28px;font-weight:500}
.member{position:absolute;width:150px;height:72px;background:var(--white);border-radius:4px;padding:12px 8px 12px 19px}
.member b{display:block;font-size:14px;font-weight:500;white-space:nowrap}
.member span{display:block;font-size:9.5px;color:var(--muted);line-height:14px;margin-top:4px;white-space:nowrap}

/* prototype */
.proto{top:1840px;height:576px;background:var(--dark);color:var(--white)}
.proto h2{position:absolute;left:126px;top:118px;font-size:33px;font-weight:500}
.proto .lead{left:126px;top:190px;width:340px;font-size:14px;line-height:22px;font-weight:600}
.proto .copy{left:126px;top:260px;width:360px;font-size:10.5px;line-height:22.5px;color:#ddd}
.proto .note{left:126px;top:374px;font-size:10px;font-weight:700}
.proto-btn{left:126px;top:406px;width:300px;height:55px;border-radius:8px;font-size:13px;line-height:18px;text-align:center}
.video{left:525px;top:96px;width:550px;height:385px;background:linear-gradient(160deg,#8c8e8a,#5a5c58 60%,#3f4140)}
.play{left:247px;top:164px;width:56px;height:56px;border-radius:50%;background:var(--white);display:flex;align-items:center;justify-content:center}

/* co-packing & value */
.sec-title{font-size:36px;font-weight:500;color:var(--orange);padding-left:18px;border-left:8px solid var(--slate);line-height:34px}
.sec-lead{font-size:13.5px;line-height:22px;font-weight:600}
.sec-copy{font-size:10.5px;line-height:22.5px;color:var(--muted)}
.accordion{position:absolute;background:var(--slate);padding:4px 24px}
.accordion div{display:flex;justify-content:space-between;align-items:center;height:38px;color:var(--white);font-size:13px;font-weight:600;border-bottom:1px solid rgba(255,255,255,.35)}
.accordion div:last-child{border-bottom:0}
.accordion div::after{content:"+";font-size:22px;font-weight:300}
.copack{top:2416px;height:620px}
.copack-photo{left:549px;top:81px;width:525px;height:463px;background:linear-gradient(135deg,#7fdc3d,#c44b3d 45%,#d4b78f)}
.value{top:3036px;height:615px}
.value-photo{left:126px;top:18px;width:507px;height:521px;background:linear-gradient(160deg,#3f5a2c,#8d6b4e 50%,#b7452f)}
.value-cta{left:716px;top:345px;width:358px;text-align:center;color:var(--orange);font-size:10.5px;font-weight:600;line-height:15px}

/* entrepreneurs */
.makers{top:3651px;height:529px;background:var(--peach);overflow:hidden}
.makers h2{position:absolute;left:126px;top:84px;font-size:33px;font-weight:500;color:var(--orange)}
.arrows{left:1015px;top:92px;display:flex;gap:26px}
.maker{position:absolute;top:158px;width:230px;height:291px;background:var(--white)}
.maker .ph{left:0;top:0;width:230px;height:230px}
.maker b{position:absolute;left:0;top:243px;width:230px;text-align:center;font-size:21px;font-weight:500}

/* footer */
.footer{top:4180px;height:313px;background:var(--dark);color:var(--white)}
.f-brand{left:126px;top:90px;display:flex;align-items:center;gap:12px}
.f-brand i{width:90px;height:90px;border-radius:50%;background:var(--white);display:block}
.f-brand b{font-size:22px;font-weight:700}
.f-head{font-size:10px;font-weight:700;letter-spacing:.5px}
.f-col{font-size:10.5px;line-height:18px}
.f-col p{display:flex;gap:14px;margin-bottom:8px}
.f-social{left:404px;top:221px;display:flex;gap:10px}
.f-social i{width:22px;height:22px;border-radius:50%;background:var(--orange);display:block}
.field{position:absolute;height:32px;border-radius:8px;background:#6a6a6a;font-size:10px;color:#ccc;padding:10px 20px}
.sub-btn{left:958px;top:167px;width:116px;height:32px;border-radius:8px;font-size:11px}
.cards{left:720px;top:222px;display:flex;gap:6px}
.cards i{width:36px;height:22px;border-radius:3px;background:#e8e8e8;display:block}
.bottom{top:4493px;height:76px;background:var(--white)}
.bottom p{position:absolute;left:126px;top:30px;font-size:10px;color:var(--muted)}
</style>
</head>
<body>

<header class="block site-header">
  <div class="abs brand"><span class="brand-dot"></span><span class="brand-name">ERPWH</span></div>
  <div class="abs contact-line">
    <span><svg width="12" height="12" viewBox="0 0 24 24"><path d="M6 2l4 4-2 3c1 3 4 6 7 7l3-2 4 4-3 4C10 21 3 14 2 5z" fill="none" stroke="#d8602a" stroke-width="2"/></svg>555-201-4480</span>
    <span><svg width="14" height="11" viewBox="0 0 24 18"><rect x="1" y="1" width="22" height="16" fill="none" stroke="#d8602a" stroke-width="2"/><path d="M1 1l11 9 11-9" fill="none" stroke="#d8602a" stroke-width="2"/></svg>nora@erpwh.org, jules@erpwh.org,</span>
  </div>
  <div class="abs social-top"><i></i><i></i><i></i></div>
  <nav class="abs nav"><span>ABOUT</span><span>PROTOTYPE</span><span>CO PACKING</span><span>VALUE ADD</span><span>OUR ENTREPRENEURS</span></nav>
  <div class="btn header-btn">Get In Touch <svg width="12" height="12" viewBox="0 0 12 12"><circle cx="6" cy="6" r="5" fill="none" stroke="#fff"/><path d="M5 4l2 2-2 2" fill="none" stroke="#fff"/></svg></div>
</header>

<section class="block hero" role="img" aria-label="Farm workers harvesting on green terraced hillside fields">
  <h1 class="abs hero-title">Eastern Ridge Produce Works Hub</h1>
  <div class="btn hero-btn">Get In Touch <svg width="12" height="12" viewBox="0 0 12 12"><circle cx="6" cy="6" r="5" fill="none" stroke="#fff"/><path d="M5 4l2 2-2 2" fill="none" stroke="#fff"/></svg></div>
  <div class="abs watch"><span class="watch-dot"><svg width="12" height="12" viewBox="0 0 12 12"><path d="M3 1l8 5-8 5z" fill="#fff"/></svg></span>Watch Video</div>
</section>

<div class="abs mission">
  <div class="ph mission-photo" role="img" aria-label="Crates of fresh red tomatoes in a processing room"></div>
  <p class="abs mission-text">Promoting economic development through entrepreneurship, providing opportunities for sustaining local agriculture, and promoting best practices for food producers</p>
</div>

<section class="block about">
  <div class="ph about-photo-a" role="img" aria-label="Hand holding a jar of tomato sauce"></div>
  <div class="ph about-photo-b" role="img" aria-label="Rack of jarred tomato sauce on shelves"></div>
  <p class="abs eyebrow">About Us</p>
  <h2 class="abs about-title"><em>Welcome To</em> Eastern Ridge Produce Works Hub</h2>
  <p class="abs about-copy">The Eastern Ridge Produce Works Hub was created in 2001 to support new and growing food businesses as they navigate the path of bringing a food product to market. Our mission is to promote economic development through entrepreneurship, provide opportunities for sustaining local agriculture, and promote best practices for food producers. The ERPWH offers rental manufacturing space as well as co-packing services to food businesses in the commonwealth and beyond. We also work with local farms to make value-added products, like jams, sauces, pickles and purees. In addition to these services, our team also provides one-on-one counseling and technical assistance, supporting you with business planning, product development, regulatory compliance, food safety and more.</p>
</section>

<section class="block team">
  <h2>Our Team</h2>
  <div class="member" style="left:365px;top:131px"><b>Nora Bexley</b><span>Director of Operations<br>555-201-4480 ext.110</span></div>
  <div class="member" style="left:525px;top:131px"><b>Jules Marlow</b><span>Food Business Manager<br>555-201-4480 ext.104</span></div>
  <div class="member" style="left:685px;top:131px"><b>Trent Odell</b><span>Floor Supervisor</span></div>
  <div class="member" style="left:365px;top:213px"><b>Rafi Duarte</b><span>Production Team Leader</span></div>
  <div class="member" style="left:525px;top:213px"><b>Owen Pell</b><span>Operations Team Leader</span></div>
  <div class="member" style="left:685px;top:213px"><b>Martin Krause</b><span>Production Worker</span></div>
  <div class="member" style="left:365px;top:294px"><b>Dario Lunt</b><span>Sanitation Specialist</span></div>
  <div class="member" style="left:525px;top:294px"><b>Ivo Carrane</b><span>Production Worker</span></div>
  <div class="member" style="left:685px;top:294px"><b>Luis Serrano</b><span>Production Worker</span></div>
</section>

<section class="block proto">
  <h2>Prototype My Food</h2>
  <p class="abs lead">Are you an entrepreneur with a stellar recipe? Ready to commercial and scale?</p>
  <p class="abs copy">Schedule a prototype with our team. We will work with you to turn your recipe into a commercial formula, select appropriate packaging, create a compliant label, and create a prototype of your product. Please submit an interest form to connect with our team.</p>
  <p class="abs note">The ERPWH offers prototyping services from November-May.</p>
  <div class="btn proto-btn">Learn more about launching<br>a food business here</div>
  <div class="ph video" role="img" aria-label="Video still of two workers in masks carrying boxes in a parking lot">
    <div class="abs play"><svg width="18" height="18" viewBox="0 0 12 12"><path d="M3.5 1.5l7 4.5-7 4.5z" fill="#d8602a"/></svg></div>
  </div>
</section>

<section class="block copack">
  <h2 class="abs sec-title" style="left:120px;top:134px">Co-Packing</h2>
  <p class="abs sec-lead" style="left:126px;top:184px;width:260px">Are you an established business looking for co-packing support? <span style="color:var(--orange)">We can help!</span></p>
  <p class="abs sec-copy" style="left:126px;top:276px;width:355px">The ERPWH specializes in hot pack and hold processing for shelf-stable prepared and acidified foods. Additionally, we offer slow and individual-quick-freeze processing. If your food product doesn't fit into these categories, please give us a call to discuss. If it does, please submit an interest form to connect with our team.</p>
  <div class="accordion" style="left:126px;top:429px;width:356px"><div>What to expect</div><div>Pricing</div><div>Other qualifications and services</div></div>
  <div class="ph copack-photo" role="img" aria-label="Green buckets of red apples beside cardboard produce boxes"></div>
</section>

<section class="block value">
  <div class="ph value-photo" role="img" aria-label="Hand holding a jar of preserved pasta sauce against greenery"></div>
  <h2 class="abs sec-title" style="left:711px;top:58px">Value-Added</h2>
  <p class="abs sec-lead" style="left:716px;top:112px">Turn your crops into value-added products!</p>
  <p class="abs sec-copy" style="left:716px;top:158px;width:358px">The Eastern Ridge Produce Works Hub can turn your crops into value added products. We offer 12 recipes for products that will feature your tomatoes, peppers, cukes, root veggies, apples and more! Farmers deliver the key ingredient(s) to Ashbrook and the ERPWH team will process, bottle, label and pack for you. We provide bottle, lid, label and case. Farmers sell finished product at their farms stands, as part of CSA's and in the wholesale market.</p>
  <p class="abs value-cta">Contact Jules today to learn more<br>jules@erpwh.org or 555-201-4480, ext. 104</p>
  <div class="accordion" style="left:716px;top:408px;width:358px"><div>Value-Added Products</div><div>FAQ's</div><div>Flash Freezing Options for Farms</div></div>
</section>

<section class="block makers">
  <h2>Meet Our Entrepreneurs</h2>
  <div class="abs arrows">
    <svg width="14" height="22" viewBox="0 0 14 22"><path d="M11 2L3 11l8 9" fill="none" stroke="#d8602a" stroke-width="2.5"/></svg>
    <svg width="14" height="22" viewBox="0 0 14 22"><path d="M3 2l8 9-8 9" fill="none" stroke="#d8602a" stroke-width="2.5"/></svg>
  </div>
  <div class="maker" style="left:126px"><div class="ph" style="background:linear-gradient(150deg,#2e3a4f,#6b6a80)" role="img" aria-label="Bottle of elderberry syrup with lavender"></div><b>Quiet Meadow</b></div>
  <div class="maker" style="left:365px"><div class="ph" style="background:linear-gradient(150deg,#d9474a,#f3eeee)" role="img" aria-label="Farm graphic with tree roots on a red background"></div><b>Plain Bounty Farm</b></div>
  <div class="maker" style="left:606px"><div class="ph" style="background:radial-gradient(circle at 50% 55%,#b26a20,#f1f1f1 70%)" role="img" aria-label="Jar of turmeric honey"></div><b>Old Barn Farm</b></div>
  <div class="maker" style="left:845px"><div class="ph" style="background:linear-gradient(150deg,#f4f4f4,#c1402a 55%,#f0f0f0)" role="img" aria-label="Three bottles of maple syrup"></div><b>Sugarline Foods</b></div>
  <div class="maker" style="left:1085px"><div class="ph" style="background:linear-gradient(150deg,#e8d7d0,#c8665a)" role="img" aria-label="Jars of preserves"></div><b>Hearth Row</b></div>
</section>

<footer class="block footer">
  <div class="abs f-brand"><i></i><b>ERPWH</b></div>
  <p class="abs f-head" style="left:404px;top:64px">OUR CONTACT</p>
  <div class="abs f-col" style="left:404px;top:96px">
    <p><svg width="10" height="12" viewBox="0 0 24 24"><path d="M6 2l4 4-2 3c1 3 4 6 7 7l3-2 4 4-3 4C10 21 3 14 2 5z" fill="none" stroke="#d8602a" stroke-width="2.5"/></svg>555-201-4480</p>
    <p><svg width="10" height="12" viewBox="0 0 20 24"><path d="M10 23S2 14 2 9a8 8 0 0116 0c0 5-8 14-8 14z" fill="none" stroke="#d8602a" stroke-width="2.5"/><circle cx="10" cy="9" r="3" fill="#d8602a"/></svg>88 Mill Lane, Ashbrook, MA 01399</p>
    <p><svg width="10" height="10" viewBox="0 0 24 18"><rect x="1" y="1" width="22" height="16" fill="none" stroke="#d8602a" stroke-width="2.5"/><path d="M1 1l11 9 11-9" fill="none" stroke="#d8602a" stroke-width="2.5"/></svg><span><b>Nora Bexley,</b> nora@erpwh.org<br><b>Jules Marlow,</b> jules@erpwh.org,</span></p>
  </div>
  <div class="abs f-social"><i></i><i></i><i></i><i></i><i></i></div>
  <p class="abs f-head" style="left:720px;top:64px">NEWSLETTER</p>
  <p class="abs f-col" style="left:720px;top:92px">Register here for our ERPWH Food Safety Newsletter:</p>
  <div class="field" style="left:720px;top:121px;width:354px">Full Name</div>
  <div class="field" style="left:720px;top:167px;width:228px">Email</div>
  <div class="btn sub-btn">Subscribe</div>
  <div class="abs cards"><i></i><i></i><i></i><i></i><i></i></div>
</footer>

<div class="block bottom"><p>Copyright 2022 Eastern Ridge Produce Works Hub All rights reserved.</p></div>

</body>
</html>
```